MORLO's Coffee Liqueur Shot Arabica

Need a lable for a 500ml bottle of homemade Coffee liqueur.
Name:
MORLO's
Coffee
Shot

Shape: Round, 80mm
Color of the lable should be black and letters in black.
Letters MORLO's min 12mm hight.
Color of the liqueur is dark brown.
Add: 500ml
Add: 38% vol.
Should have a bean on the lable.
Maybe some bullet words on the bottom...
Prefered design see Pic1a with bottle.

Target Market(s)

People that enjoy coffee in shots, in coctails, with ice or on top of icecream or any other dessert

Font styles to use
Serif

Colors

Designer to choose colors to be used in the design.

Requirements
Must have
• See Pic 1a
Nice to have
• See Pic1a (bottle)
Should not have
• Different colors

```html
<!DOCTYPE html>
<html lang="en">
<head>
<meta charset="utf-8">
<title>MORLO's Coffee Shot – Round Label</title>
<link rel="stylesheet" href="https://fonts.googleapis.com/css2?family=Alfa+Slab+One&family=Ubuntu+Condensed&family=Ubuntu:wght@700&display=swap">
<style>
  :root {
    --backdrop: #e8e8e6;
    --label-paper: #f5f5f3;
    --ink: #1d1d1d;
  }
  html, body {
    margin: 0;
    padding: 0;
    width: 1200px;
    height: 960px;
    overflow: hidden;
    background: var(--backdrop);
  }
  .stage {
    width: 1200px;
    height: 960px;
    display: flex;
    align-items: center;
    justify-content: center;
  }
  .round-label {
    width: 820px;
    height: 820px;
    border-radius: 50%;
    background: var(--label-paper);
    display: flex;
    flex-direction: column;
    align-items: center;
    justify-content: center;
    box-sizing: border-box;
    color: var(--ink);
  }
  .brand-name {
    margin: 0;
    font-family: "Alfa Slab One", serif;
    font-weight: 400;
    font-size: 76px;
    line-height: 1;
    letter-spacing: 6px;
  }
  .rule {
    width: 700px;
    height: 12px;
    border-radius: 6px;
    background: var(--ink);
  }
  .rule-top { margin-top: 34px; }
  .product-row {
    width: 700px;
    display: grid;
    grid-template-columns: 1fr auto 1fr;
    align-items: center;
    padding: 14px 0;
  }
  .spec {
    font-family: "Ubuntu", sans-serif;
    font-weight: 700;
    font-size: 26px;
  }
  .spec-volume { justify-self: start; padding-left: 18px; }
  .spec-alcohol { justify-self: end; padding-right: 18px; }
  .product-name {
    margin: 0;
    font-family: "Ubuntu Condensed", sans-serif;
    font-weight: 400;
    font-size: 88px;
    line-height: 0.95;
    text-align: center;
  }
  .bean-area {
    width: 70px;
    height: 96px;
    margin-top: 30px;
    border-radius: 50%;
    background: var(--ink);
    transform: rotate(35deg);
  }
  .tagline {
    margin: 30px 0 0;
    font-family: "Alfa Slab One", serif;
    font-size: 38px;
    letter-spacing: 3px;
    word-spacing: 60px;
  }
</style>
</head>
<body>
<main class="stage">
  <section class="round-label" aria-label="MORLO's Coffee Shot round label">
    <h1 class="brand-name">MORLO’S</h1>
    <div class="rule rule-top"></div>
    <div class="product-row">
      <span class="spec spec-alcohol">38%Vol</span>
      <h2 class="product-name">Coffee<br>Shot</h2>
      <span class="spec spec-volume">500ml</span>
    </div>
    <div class="rule"></div>
    <div class="bean-area" role="img" aria-label="Coffee bean illustration"></div>
    <p class="tagline">ARABICA INTENSE</p>
  </section>
</main>
</body>
</html>
```